technical refinement that graphics look less AI-generated and more professional/corporate

We have a set of graphics and diagrams that were initially created using AI. The content, structure, and overall layout are already defined and should remain largely unchanged.

The objective is NOT to create completely new designs. This is primarily a technical refinement and conversion project. The graphics need to be professionally redrawn, cleaned up, and rebuilt so that they:

• Look less AI-generated and more professional/corporate
• Match our existing corporate website style
• Are fully editable in Microsoft PowerPoint
• Use consistent fonts, colors, spacing, and iconography
• Maintain the original meaning and information structure

REFERENCE WEBSITE
https://kraftwerkstatt-auenfeld. at/

Please use the website as the primary reference for:
• Color palette
• Typography
• Visual language
• General corporate look and feel
• Professional, research-oriented appearance

The style should be clean, technical, modern, and suitable for a scientific/research institution.

```html
<!DOCTYPE html>
<html lang="en">
<head>
<meta charset="utf-8">
<title>Energy Research Institute – Overview Graphics</title>
<link rel="stylesheet" href="https://fonts.googleapis.com/css2?family=Open+Sans:wght@400;600;700;800&display=swap">
<style>
  :root {
    --green-900: #17562a;
    --green-800: #1f6b2e;
    --green-600: #4c9a3e;
    --green-500: #6fab3f;
    --green-400: #8cc63f;
    --green-300: #a3cb3c;
    --tint: #eef4ea;
    --tint-strong: #e2eddb;
    --band: #e4e7e4;
    --fossil: #9b9b9b;
    --text: #3a3f3b;
    --muted: #555b56;
    --rule: #dcdfdc;
    --white: #ffffff;
  }
  * { box-sizing: border-box; margin: 0; padding: 0; }
  html, body { width: 1200px; height: 655px; overflow: hidden; background: var(--white); }
  body {
    font-family: "Open Sans", Arial, sans-serif;
    color: var(--text);
    display: grid;
    grid-template-columns: repeat(3, 396px);
    grid-template-rows: 344px 305px;
    gap: 6px;
  }
  .panel { position: relative; border: 1px solid var(--rule); background: var(--white); overflow: hidden; }
  .abs { position: absolute; }
  .panel-title { position: absolute; left: 23px; top: 16px; font-size: 17px; font-weight: 700; color: var(--green-800); letter-spacing: .2px; }
  .panel-title.small { font-size: 12px; top: 20px; left: 21px; }
  .panel-subtitle { position: absolute; left: 23px; top: 41px; font-size: 12px; color: var(--muted); }
  .title-rule { position: absolute; left: 23px; top: 41px; width: 46px; height: 2px; background: var(--green-400); }
  .title-rule.low { top: 39px; left: 21px; }
  .icon { width: 24px; height: 24px; fill: none; stroke: currentColor; stroke-width: 1.6; stroke-linecap: round; stroke-linejoin: round; }
  .nowrap { white-space: nowrap; }

  /* competence areas */
  .flower { position: absolute; left: 0; top: 0; }
  .core-label { position: absolute; left: 150px; top: 148px; width: 100px; text-align: center; font-size: 11.5px; line-height: 14px; font-weight: 700; color: var(--green-800); }
  .area { position: absolute; white-space: nowrap; }
  .area.right-aligned { text-align: right; }
  .area-name { font-size: 10px; font-weight: 700; color: var(--green-800); line-height: 12px; }
  .area-text { margin-top: 4px; font-size: 7px; line-height: 9.5px; color: var(--muted); }
  .petal-icon { position: absolute; width: 30px; height: 30px; color: var(--green-800); margin: -15px 0 0 -15px; }
  .petal-icon svg { width: 30px; height: 30px; }
  .paragraph-sign { position: absolute; font-size: 28px; font-weight: 600; color: var(--green-800); transform: translate(-50%, -55%); }

  /* energy transition */
  .phase { position: absolute; top: 160px; width: 110px; margin-left: -55px; text-align: center; }
  .phase-name { font-size: 9px; font-weight: 700; line-height: 11px; color: #444; }
  .phase-name.is-green { color: var(--green-600); }
  .phase-name.is-dark { color: var(--green-800); }
  .phase-text { margin-top: 11px; font-size: 8px; line-height: 10.5px; color: var(--muted); }
  .statement { position: absolute; left: 22px; top: 262px; width: 350px; height: 52px; background: var(--tint); border-radius: 3px; display: flex; align-items: center; gap: 14px; padding: 0 14px; }
  .statement .icon { width: 28px; height: 28px; color: var(--green-800); flex: none; }
  .statement p { font-size: 9px; line-height: 12.5px; color: #333; }

  /* research approach */
  .step { position: absolute; white-space: nowrap; }
  .step-name { font-size: 9px; font-weight: 700; color: var(--green-800); }
  .step-text { margin-top: 5px; font-size: 7.5px; line-height: 10px; color: #333; }
  .hub-label { position: absolute; left: 141px; top: 150px; width: 100px; text-align: center; font-size: 14px; line-height: 16.5px; font-weight: 700; color: var(--green-800); }

  /* impact areas */
  .impact-card { position: absolute; width: 171px; height: 68px; background: var(--tint); border-radius: 3px; display: flex; gap: 12px; padding: 14px 6px 0 14px; }
  .impact-card .icon { width: 28px; height: 28px; flex: none; color: var(--green-800); stroke-width: 1.4; }
  .impact-name { font-size: 8.5px; font-weight: 700; color: var(--green-800); margin-top: 2px; white-space: nowrap; }
  .impact-text { margin-top: 4px; font-size: 7.5px; line-height: 10.5px; color: #444; white-space: nowrap; }

  /* projects */
  .project { position: absolute; left: 21px; width: 351px; display: flex; background: var(--tint); border-radius: 3px; overflow: hidden; }
  .project-info { width: 177px; display: flex; align-items: center; gap: 12px; padding-left: 7px; }
  .project-badge { width: 54px; height: 54px; border-radius: 50%; display: grid; place-items: center; color: var(--white); flex: none; }
  .project-badge .icon { width: 28px; height: 28px; stroke-width: 1.5; }
  .badge-light { background: linear-gradient(135deg, #8cc63f, #5aa332); }
  .badge-dark { background: var(--green-800); }
  .project-name { font-size: 9px; font-weight: 700; line-height: 12px; color: var(--green-800); }
  .project-text { margin-top: 3px; font-size: 7.5px; line-height: 10.5px; color: #333; white-space: nowrap; }
  .project-visual { flex: 1; }
  .visual-city { background: linear-gradient(180deg, #d9dfe2 0%, #c4c9c6 40%, #7f9c67 75%, #5f8a47 100%); }
  .visual-plant { background: linear-gradient(180deg, #cfd8de 0%, #b8bfc4 45%, #8e979c 80%, #6c7377 100%); }
  .visual-storage { background: linear-gradient(180deg, #cddfe9 0%, #e8ecee 40%, #c9cdcf 75%, #7a8a5a 100%); }

  /* key figures */
  .figure-card { position: absolute; width: 98px; height: 109px; background: var(--tint); border-radius: 3px; text-align: center; padding-top: 15px; color: var(--green-800); }
  .figure-card .icon { width: 30px; height: 30px; stroke-width: 1.4; }
  .figure-value { margin-top: 8px; font-size: 18px; font-weight: 700; line-height: 20px; }
  .figure-label { margin-top: 3px; font-size: 8px; line-height: 11px; color: #444; }
</style>
</head>
<body>

<svg width="0" height="0" style="position:absolute" aria-hidden="true">
  <defs>
    <symbol id="i-building" viewBox="0 0 24 24"><path d="M3 21h18M5 21V9h6v12M11 21V4h8v17M7 12h2M7 15h2M7 18h2M13 7h2M16 7h1M13 10h2M16 10h1M13 13h2M16 13h1M13 16h2M16 16h1"/></symbol>
    <symbol id="i-turbine" viewBox="0 0 24 24"><path d="M12 10v11M9 21h6M12 10V2M12 10l-7 5M12 10l7 5"/><circle cx="12" cy="10" r="1.2"/></symbol>
    <symbol id="i-network" viewBox="0 0 24 24"><circle cx="12" cy="12" r="2.6"/><circle cx="4.5" cy="5" r="1.8"/><circle cx="19.5" cy="5" r="1.8"/><circle cx="4.5" cy="19" r="1.8"/><circle cx="19.5" cy="19" r="1.8"/><circle cx="21" cy="12" r="1.4"/><path d="M6 6.3l4 3.8M18 6.3l-4 3.8M6 17.7l4-3.8M18 17.7l-4-3.8M14.6 12h5"/></symbol>
    <symbol id="i-battery" viewBox="0 0 24 24"><rect x="7" y="4.5" width="10" height="17" rx="1.8"/><path d="M10 2.5h4"/><rect x="9.3" y="8" width="5.4" height="11" fill="currentColor" stroke="none"/></symbol>
    <symbol id="i-car" viewBox="0 0 24 24"><path d="M2.5 17v-3.5l2-1 2-4h8l3 4 4 1V17z" fill="currentColor"/><path d="M7.5 9.8h3v2.4H5.8zM12 9.8h2.4l1.6 2.4h-4z" fill="#fff" stroke="none"/><circle cx="7" cy="17.5" r="2" fill="#fff"/><circle cx="17" cy="17.5" r="2" fill="#fff"/><path d="M18 8V5.5h3M21 3.5v4"/></symbol>
    <symbol id="i-globe" viewBox="0 0 24 24"><circle cx="12" cy="12" r="9.5"/><ellipse cx="12" cy="12" rx="4.2" ry="9.5"/><path d="M2.5 12h19M4 7h16M4 17h16"/></symbol>
    <symbol id="i-chart" viewBox="0 0 24 24"><path d="M3 3v18h18M6 17l4-5 3 3 6-7M16 8h3v3"/></symbol>
    <symbol id="i-leaf" viewBox="0 0 24 24"><path d="M4.5 19.5C4.5 10 10.5 4 20 4c0 9.5-6 15.5-15.5 15.5zM4.5 19.5l9-9"/></symbol>
    <symbol id="i-people" viewBox="0 0 24 24"><circle cx="5.5" cy="7" r="2.3"/><circle cx="12" cy="7" r="2.3"/><circle cx="18.5" cy="7" r="2.3"/><path d="M1.5 15a4 4 0 0 1 8 0M8 15a4 4 0 0 1 8 0M14.5 15a4 4 0 0 1 8 0M3.5 21a4 4 0 0 1 8 0M12.5 21a4 4 0 0 1 8 0"/></symbol>
    <symbol id="i-gear" viewBox="0 0 24 24"><circle cx="12" cy="12" r="3.2"/><path d="M10.3 2.5h3.4l.5 2.7 1.9.8 2.3-1.6 2.4 2.4-1.6 2.3.8 1.9 2.7.5v3.4l-2.7.5-.8 1.9 1.6 2.3-2.4 2.4-2.3-1.6-1.9.8-.5 2.7h-3.4l-.5-2.7-1.9-.8-2.3 1.6-2.4-2.4 1.6-2.3-.8-1.9-2.7-.5v-3.4l2.7-.5.8-1.9-1.6-2.3 2.4-2.4 2.3 1.6 1.9-.8z"/></symbol>
    <symbol id="i-cap" viewBox="0 0 24 24"><path d="M1.5 9L12 4l10.5 5L12 14zM6 11.2v5.3c3.5 2.6 8.5 2.6 12 0v-5.3M21 9.5v5"/></symbol>
    <symbol id="i-search" viewBox="0 0 24 24"><circle cx="10" cy="10" r="6.5"/><path d="M14.8 14.8L21 21"/></symbol>
    <symbol id="i-bulb" viewBox="0 0 24 24"><path d="M12 6a5 5 0 0 0-3 9v2.5h6V15a5 5 0 0 0-3-9zM10 20h4M12 1.5v2M4 4.5l1.5 1.5M20 4.5L18.5 6M2 11h2M20 11h2"/></symbol>
    <symbol id="i-chat" viewBox="0 0 24 24"><path d="M12 3.5c5.2 0 9 3.3 9 7.5s-3.8 7.5-9 7.5c-1.2 0-2.3-.2-3.3-.5L4 20l1.2-4C3.8 14.7 3 13 3 11c0-4.2 3.8-7.5 9-7.5z"/></symbol>
    <symbol id="i-factory" viewBox="0 0 24 24"><path d="M2 21V11l6 3.5V11l6 3.5V3h3v6h2V3h3v18z"/><path d="M5 18h2M10 18h2M15 18h2" stroke="#9b9b9b"/></symbol>
    <symbol id="i-city" viewBox="0 0 24 24"><path d="M2 21h20M4 21V9h6v12M10 21V3h8v18M6 12h2M6 15h2M12 6h2M15 6h1M12 9h2M15 9h1M12 12h2M15 12h1M18 19c0-4 2-6 4-6 0 3-2 5-4 6z"/></symbol>
    <symbol id="i-flask" viewBox="0 0 24 24"><path d="M9 2.5h6M10 2.5v6L4.5 19a1.5 1.5 0 0 0 1.3 2.3h12.4a1.5 1.5 0 0 0 1.3-2.3L14 8.5v-6"/><path d="M7 15h10l2 4.5H5z" fill="currentColor"/></symbol>
    <symbol id="i-doc" viewBox="0 0 24 24"><path d="M5 2.5h9.5L19 7v14.5H5zM14.5 2.5V7H19M8 11h8M8 14h8M8 17h8"/></symbol>
    <symbol id="i-handshake" viewBox="0 0 24 24"><path d="M1.5 8.5l4-3 5 1.5M22.5 8.5l-4-3-6 2.5-3 3 1.5 1.5 3-1.5 6 5.5M1.5 8.5L6 15l6 5 2-1.5 2 1 2-1.5 2 .5-1.5-2.5M9 17l2-2M11.5 19l2-2"/></symbol>
    <symbol id="i-calendar" viewBox="0 0 24 24"><rect x="3" y="4.5" width="18" height="17" rx="1.5"/><path d="M3 9h18M8 2.5v4M16 2.5v4M14 17.5l.01 0M17 14l.01 0M11 19l.01 0"/></symbol>
    <symbol id="i-bolt-battery" viewBox="0 0 24 24"><rect x="6.5" y="4" width="11" height="17.5" rx="1.8"/><path d="M10 2h4M12.8 7.5L9.8 13h4.4l-3 5.5"/></symbol>
  </defs>
</svg>

<!-- Competence areas -->
<section class="panel">
  <h2 class="panel-title">OUR COMPETENCE AREAS</h2>
  <span class="title-rule"></span>
  <svg class="flower" width="396" height="344" viewBox="0 0 396 344" aria-hidden="true">
    <g fill="none" stroke="var(--tint-strong)">
      <circle cx="200" cy="182" r="78" stroke-width="64" stroke-dasharray="76.2 500" transform="rotate(-148 200 182)"/>
      <circle cx="200" cy="182" r="78" stroke-width="64" stroke-dasharray="76.2 500" transform="rotate(-88 200 182)"/>
      <circle cx="200" cy="182" r="78" stroke-width="64" stroke-dasharray="76.2 500" transform="rotate(32 200 182)"/>
      <circle cx="200" cy="182" r="78" stroke-width="64" stroke-dasharray="76.2 500" transform="rotate(92 200 182)"/>
      <circle cx="200" cy="182" r="69" stroke-width="46" stroke-dasharray="67.4 500" transform="rotate(-28 200 182)"/>
      <circle cx="200" cy="182" r="69" stroke-width="46" stroke-dasharray="67.4 500" transform="rotate(152 200 182)"/>
    </g>
    <circle cx="200" cy="182" r="44" fill="var(--white)"/>
  </svg>
  <p class="core-label">WE<br>RESEARCH<br>FOR THE<br>ENERGY<br>TRANSITION</p>

  <span class="petal-icon" style="left:158px;top:111px"><svg class="icon"><use href="#i-building"/></svg></span>
  <span class="petal-icon" style="left:242px;top:111px"><svg class="icon"><use href="#i-turbine"/></svg></span>
  <span class="petal-icon" style="left:269px;top:182px"><svg class="icon"><use href="#i-network"/></svg></span>
  <span class="petal-icon" style="left:242px;top:253px"><svg class="icon"><use href="#i-battery"/></svg></span>
  <span class="petal-icon" style="left:158px;top:253px"><svg class="icon"><use href="#i-car"/></svg></span>
  <span class="paragraph-sign" style="left:131px;top:182px">§</span>

  <div class="area right-aligned" style="right:294px;top:78px">
    <p class="area-name">Sustainable<br>Buildings</p>
    <p class="area-text">Energy efficiency and<br>sustainable construction<br>for the building sector</p>
  </div>
  <div class="area" style="left:302px;top:78px">
    <p class="area-name">Renewable<br>Energy Systems</p>
    <p class="area-text">Integration and<br>optimization of<br>renewable energy<br>systems</p>
  </div>
  <div class="area right-aligned" style="right:314px;top:172px">
    <p class="area-name">Energy<br>Policy &amp;<br>Economics</p>
    <p class="area-text">Analyses and strategies<br>for sustainable<br>energy policies</p>
  </div>
  <div class="area" style="left:317px;top:178px">
    <p class="area-name">Energy<br>Networks</p>
    <p class="area-text">Smart grids and<br>efficient energy<br>infrastructures</p>
  </div>
  <div class="area right-aligned" style="right:290px;top:254px">
    <p class="area-name">Mobility<br>&amp; Transport</p>
    <p class="area-text">Sustainable mobility<br>solutions and<br>transport concepts</p>
  </div>
  <div class="area" style="left:283px;top:254px">
    <p class="area-name">Energy<br>Storage</p>
    <p class="area-text">Technologies and<br>systems for efficient<br>energy storage</p>
  </div>
</section>

<!-- Energy transition -->
<section class="panel">
  <h2 class="panel-title">THE ENERGY TRANSITION</h2>
  <p class="panel-subtitle">Our Path to a Sustainable Future</p>
  <svg class="abs" style="left:0;top:0" width="396" height="200" viewBox="0 0 396 200" aria-hidden="true">
    <rect x="24" y="112" width="330" height="12" rx="6" fill="var(--band)"/>
    <path d="M350 102l22 16-22 16z" fill="var(--band)"/>
    <circle cx="67" cy="118" r="29" fill="var(--fossil)"/>
    <circle cx="179" cy="118" r="29" fill="var(--green-400)"/>
    <circle cx="289" cy="118" r="29" fill="var(--green-800)"/>
    <g fill="none" stroke-linecap="round" stroke-linejoin="round">
      <use href="#i-factory" x="54" y="105" width="26" height="26" fill="#f3f3f3" stroke="none"/>
      <use href="#i-turbine" x="165" y="104" width="28" height="28" stroke="#fff" stroke-width="1.7"/>
      <use href="#i-leaf" x="276" y="105" width="26" height="26" stroke="#fff" stroke-width="1.6"/>
    </g>
  </svg>
  <div class="phase" style="left:67px">
    <p class="phase-name">FOSSIL<br><span style="font-weight:600">ENERGY SYSTEM</span></p>
    <p class="phase-text">Centralized,<br>fossil-based,<br>high emissions</p>
  </div>
  <div class="phase" style="left:179px">
    <p class="phase-name is-green">TRANSITION<br>PHASE</p>
    <p class="phase-text">Increasing share<br>of renewables,<br>sector coupling,<br>efficiency</p>
  </div>
  <div class="phase" style="left:289px">
    <p class="phase-name is-dark">SUSTAINABLE<br>ENERGY SYSTEM</p>
    <p class="phase-text">Renewable,<br>decentralized,<br>climate-neutral</p>
  </div>
  <div class="statement">
    <svg class="icon"><use href="#i-people"/></svg>
    <p class="nowrap">Our research supports policy, industry and society on the way<br>to a climate-neutral and sustainable energy system.</p>
  </div>
</section>

<!-- Research approach -->
<section class="panel">
  <h2 class="panel-title">RESEARCH APPROACH</h2>
  <p class="panel-subtitle">From Research to Impact</p>
  <svg class="abs" style="left:0;top:0" width="396" height="344" viewBox="0 0 396 344" aria-hidden="true">
    <g fill="none" stroke-width="65">
      <circle cx="191" cy="178" r="79.5" stroke="var(--green-300)" stroke-dasharray="122 500" transform="rotate(181 191 178)"/>
      <circle cx="191" cy="178" r="79.5" stroke="var(--green-500)" stroke-dasharray="122 500" transform="rotate(271 191 178)"/>
      <circle cx="191" cy="178" r="79.5" stroke="var(--green-800)" stroke-dasharray="122 500" transform="rotate(1 191 178)"/>
      <circle cx="191" cy="178" r="79.5" stroke="var(--green-600)" stroke-dasharray="122 500" transform="rotate(91 191 178)"/>
    </g>
    <g fill="none" stroke="#fff" stroke-width="1.5" stroke-linecap="round" stroke-linejoin="round">
      <use href="#i-search" x="120" y="107" width="28" height="28"/>
      <use href="#i-bulb" x="234" y="107" width="28" height="28"/>
      <use href="#i-chat" x="120" y="221" width="28" height="28"/>
      <use href="#i-gear" x="234" y="221" width="28" height="28"/>
    </g>
  </svg>
  <p class="hub-label">IMPACT<br>THROUGH<br>RESEARCH</p>
  <div class="step" style="left:24px;top:92px">
    <p class="step-name">ANALYZE</p>
    <p class="step-text">We identify<br>challenges and<br>analyze complex<br>systems.</p>
  </div>
  <div class="step" style="left:306px;top:92px">
    <p class="step-name">DEVELOP</p>
    <p class="step-text">We develop<br>innovative<br>technologies and<br>solutions.</p>
  </div>
  <div class="step" style="left:24px;top:224px">
    <p class="step-name">DISSEMINATE</p>
    <p class="step-text">We transfer<br>knowledge and<br>create impact<br>in society.</p>
  </div>
  <div class="step" style="left:306px;top:224px">
    <p class="step-name">DEMONSTRATE</p>
    <p class="step-text">We test and<br>demonstrate in<br>real-world<br>applications.</p>
  </div>
</section>

<!-- Impact areas -->
<section class="panel">
  <h2 class="panel-title small">OUR IMPACT AREAS</h2>
  <div class="impact-card" style="left:20px;top:55px">
    <svg class="icon"><use href="#i-globe"/></svg>
    <div><p class="impact-name">CLIMATE PROTECTION</p><p class="impact-text">Reducing greenhouse gas<br>emissions and promoting<br>climate neutrality.</p></div>
  </div>
  <div class="impact-card" style="left:201px;top:55px">
    <svg class="icon"><use href="#i-chart"/></svg>
    <div><p class="impact-name">ENERGY EFFICIENCY</p><p class="impact-text">Improving efficiency in all<br>sectors and reducing<br>energy demand.</p></div>
  </div>
  <div class="impact-card" style="left:20px;top:133px">
    <svg class="icon"><use href="#i-leaf"/></svg>
    <div><p class="impact-name">RENEWABLE ENERGIES</p><p class="impact-text">Expanding the share of<br>renewables and ensuring<br>system integration.</p></div>
  </div>
  <div class="impact-card" style="left:201px;top:133px">
    <svg class="icon"><use href="#i-people"/></svg>
    <div><p class="impact-name">SOCIETY &amp; POLICY</p><p class="impact-text">Supporting policies and<br>empowering citizens for<br>the energy transition.</p></div>
  </div>
  <div class="impact-card" style="left:20px;top:211px">
    <svg class="icon"><use href="#i-gear"/></svg>
    <div><p class="impact-name">INNOVATION</p><p class="impact-text">Developing technologies<br>and concepts for a<br>sustainable future.</p></div>
  </div>
  <div class="impact-card" style="left:201px;top:211px">
    <svg class="icon"><use href="#i-cap"/></svg>
    <div><p class="impact-name">EDUCATION</p><p class="impact-text">Training the next generation<br>and sharing knowledge<br>for a better future.</p></div>
  </div>
</section>

<!-- Project examples -->
<section class="panel">
  <h2 class="panel-title small">SELECTED PROJECT EXAMPLES</h2>
  <article class="project" style="top:54px;height:65px">
    <div class="project-info">
      <span class="project-badge badge-light"><svg class="icon"><use href="#i-city"/></svg></span>
      <div><p class="project-name">CITY<br>TRANSITION</p><p class="project-text">Sustainable urban<br>districts and smart<br>energy solutions.</p></div>
    </div>
    <div class="project-visual visual-city" role="img" aria-label="Photo of a modern residential district with green courtyard"></div>
  </article>
  <article class="project" style="top:128px;height:66px">
    <div class="project-info">
      <span class="project-badge badge-dark"><svg class="icon"><use href="#i-turbine"/></svg></span>
      <div><p class="project-name">WIND2HEAT</p><p class="project-text">Power-to-Heat<br>integration and<br>sector coupling.</p></div>
    </div>
    <div class="project-visual visual-plant" role="img" aria-label="Photo of an industrial power-to-heat plant with steel tanks and pipes"></div>
  </article>
  <article class="project" style="top:204px;height:68px">
    <div class="project-info">
      <span class="project-badge badge-dark"><svg class="icon"><use href="#i-bolt-battery"/></svg></span>
      <div><p class="project-name">STORAGE<br>SOLUTIONS</p><p class="project-text">Innovative storage<br>technologies for<br>energy systems.</p></div>
    </div>
    <div class="project-visual visual-storage" role="img" aria-label="Photo of containerised battery storage units on a paved site"></div>
  </article>
</section>

<!-- Key figures -->
<section class="panel">
  <h2 class="panel-title small">KEY FIGURES (2023)</h2>
  <span class="title-rule low"></span>
  <div class="figure-card" style="left:24px;top:56px"><svg class="icon"><use href="#i-people"/></svg><p class="figure-value">70+</p><p class="figure-label">Employees</p></div>
  <div class="figure-card" style="left:143px;top:56px"><svg class="icon"><use href="#i-flask"/></svg><p class="figure-value">25+</p><p class="figure-label">Research<br>Projects</p></div>
  <div class="figure-card" style="left:262px;top:56px"><svg class="icon"><use href="#i-doc"/></svg><p class="figure-value">150+</p><p class="figure-label">Publications</p></div>
  <div class="figure-card" style="left:24px;top:172px"><svg class="icon"><use href="#i-handshake"/></svg><p class="figure-value">40+</p><p class="figure-label">Partner<br>Organizations</p></div>
  <div class="figure-card" style="left:143px;top:172px"><svg class="icon"><use href="#i-globe"/></svg><p class="figure-value">15</p><p class="figure-label">Countries of<br>Cooperation</p></div>
  <div class="figure-card" style="left:262px;top:172px"><svg class="icon"><use href="#i-calendar"/></svg><p class="figure-value">20+</p><p class="figure-label">Years of Research<br>Excellence</p></div>
</section>

</body>
</html>
```